Real Estate flyer for listing properties

This is a flyer to be used by the property lister (the person trying to convince property vendors to sell through us) of our real estate agency Golden Harbour (https://www.golden-harbour.example). The aim of the flyer is to convince owners to list their properties with us, so that we can advertise & sell them. We have our offices located in San Luis de Sabinillas / Manilva, Costa del Sol, Spain. The real estate market here is highly competetive and we want to stand out from our competition and establish trust, which is essential for owners to list with us.

I have attached the design of our old flyer. Please note that we would like the new flyer to use our new logo, and our colors, not the wine red color used previously

I have also added some photos of our offices and of properties we have sold. We can provide more photos on request.

1. Project Overview & Objectives
High-level goal: Convince owners in Manilva & nearby to list with us.

2. Style guidelines
Please stick with the current logo & Font. We do NOT require a logo re-design. The font for Golden Harbour is Myriad Pro Bold Italic in color #D1672E. The blue used is #65A8DE and yellow #F2E946
The flyer should be A5 size.

3. Mandatory elements
Section with agent photo, name, email address & phone number. The design should allow for the flyer to be two sided, where one side is in English, and the other side in Spanish.

4. Ideas
- Maybe include address of offices (Calle Los Pinos 8, 29601 San Luis de Sabinillas) or QR code to open on google
- Offer free valuations
- Maybe mention biggest portals we are on with logo e.g. Casaverde, Vivilar, Techos.example, Moravo, A Home By the Bay, etc
- List languages we speak (Spanish, English, German, Russian, Ukrainian, Lithuanian, French, Italian, Danish, Polish)
- We also offer: Maintenance & Key holding
- Mention we have clients waiting
Note, these are just ideas, obviously not everything can be on the flyer.

Please note that the final flyer should be good for printing, just to be updated with the agents picture and contact details. Meaning all the marketing text should be written.

5. Assets & Output
Output sizes: e.g. A5 print flyer (210 × 148 mm), plus a social-media optimized JPG (1080 × 1080 px).

File formats required: InDesign (editable), plus flattened PDF for print; JPG/PNG for web.

5. Additional task - "stationary"
We need a design for a flap folder. I have attached a photo of such a flap folder, as well as the illustrator printing guidelines from the printing company.

Feel free to message me in case you have any questions or doubts.

Industry/Entity Type

Real Estate

Requirements
Must have
• Use our company logo, color scheme (from logo)

```html
<!DOCTYPE html>
<html lang="en">
<head>
<meta charset="utf-8">
<title>Golden Harbour – Sell with us</title>
<link rel="stylesheet" href="https://fonts.googleapis.com/css2?family=Open+Sans:ital,wght@0,600;0,700;1,600;1,700;1,800&family=Barlow+Semi+Condensed:ital,wght@1,500;1,600;1,700&family=Barlow:ital,wght@1,500;1,600&display=swap">
<style>
  :root {
    --navy: #111628;
    --orange: #e8672a;
    --white: #ffffff;
    --ink: #1a1d2b;
    --grey: #4a4a4a;
    --sun: #f2c230;
    --photo-warm-a: #f3c89a;
    --photo-warm-b: #c98a5e;
    --photo-sky: #9cc6e6;
    --photo-pool: #3ca6e0;
    --photo-green: #7fa660;
    --photo-interior: #d9a35f;
  }
  * { margin: 0; padding: 0; box-sizing: border-box; }
  html, body { width: 756px; height: 1200px; overflow: hidden; background: var(--white); }
  .flyer { position: relative; width: 756px; height: 1200px; overflow: hidden; background: var(--white); font-family: "Barlow Semi Condensed", sans-serif; color: var(--ink); }
  .flyer-shapes { position: absolute; inset: 0; }
  .brand { position: absolute; left: 18px; top: 40px; width: 180px; text-align: center; }
  .brand-mark { width: 44px; height: 44px; border-radius: 50%; background: var(--sun); margin: 0 auto 10px; }
  .brand-name { font-family: "Open Sans", sans-serif; font-weight: 700; font-size: 21px; color: var(--orange); line-height: 1.1; }
  .brand-regions { font-family: "Open Sans", sans-serif; font-style: italic; font-weight: 600; font-size: 10px; color: var(--grey); margin-top: 4px; }
  .brand-web { font-family: "Open Sans", sans-serif; font-style: italic; font-weight: 600; font-size: 12px; color: var(--grey); margin-top: 2px; }
  .gallery-photo { position: absolute; left: 58px; width: 224px; height: 140px; border: 3px solid var(--white); }
  .headline { position: absolute; left: 320px; top: 372px; font-family: "Open Sans", sans-serif; font-style: italic; font-weight: 800; font-size: 62px; letter-spacing: -1.5px; color: var(--navy); white-space: nowrap; }
  .tagline { position: absolute; left: 322px; top: 451px; font-family: "Open Sans", sans-serif; font-style: italic; font-weight: 700; font-size: 25px; letter-spacing: 9px; color: var(--orange); white-space: nowrap; }
  .extra-offer { position: absolute; left: 322px; top: 516px; width: 370px; height: 76px; display: flex; flex-direction: column; justify-content: center; align-items: center; color: var(--white); font-family: "Barlow", sans-serif; font-style: italic; font-weight: 600; font-size: 20px; line-height: 1.25; text-align: center; }
  .results-title { position: absolute; left: 322px; top: 616px; font-style: italic; font-weight: 700; font-size: 25px; color: var(--navy); white-space: nowrap; }
  .results-list { position: absolute; left: 324px; top: 662px; list-style: none; font-style: italic; font-weight: 500; font-size: 12.5px; color: var(--navy); }
  .results-group { margin-bottom: 8px; }
  .results-group > span { display: block; font-weight: 600; height: 24px; line-height: 24px; }
  .results-point { position: relative; height: 24px; line-height: 24px; padding-left: 24px; white-space: nowrap; }
  .results-point svg { position: absolute; left: 7px; top: 8px; }
  .valuation-badge { position: absolute; left: 347px; top: 970px; width: 212px; height: 122px; }
  .valuation-text { position: absolute; left: 372px; top: 1006px; font-family: "Open Sans", sans-serif; font-style: italic; font-weight: 600; color: var(--white); font-size: 26px; line-height: 0.98; letter-spacing: 1px; }
  .valuation-text span { display: block; font-size: 24px; letter-spacing: 2.5px; }
  .agent-photo { position: absolute; left: 668px; top: 966px; width: 88px; height: 136px; background: linear-gradient(180deg, #ffffff 0%, #ffffff 35%, #2c3b5c 36%, #1c2640 100%); border-radius: 44px 44px 0 0; }
  .agent-name { position: absolute; left: 540px; top: 1101px; width: 216px; height: 44px; line-height: 44px; text-align: center; font-family: "Open Sans", sans-serif; font-style: italic; font-weight: 700; font-size: 22px; letter-spacing: 2.5px; color: var(--white); white-space: nowrap; }
  .footer-offices { position: absolute; left: 40px; top: 1156px; color: var(--white); font-style: italic; font-weight: 500; line-height: 1.35; }
  .footer-offices p:first-child { font-size: 11.5px; letter-spacing: 0.3px; }
  .footer-offices p:last-child { font-size: 8.5px; }
  .footer-contact { position: absolute; left: 548px; top: 1150px; width: 196px; text-align: center; color: var(--white); font-style: italic; font-weight: 500; font-size: 10px; line-height: 1.3; }
</style>
</head>
<body>
<main class="flyer">
  <svg class="flyer-shapes" width="756" height="1200" viewBox="0 0 756 1200" aria-hidden="true">
    <defs>
      <linearGradient id="storefront-tones" x1="0" y1="0" x2="1" y2="1">
        <stop offset="0" stop-color="#fbe9d4"/>
        <stop offset="0.4" stop-color="var(--photo-warm-a)"/>
        <stop offset="1" stop-color="var(--photo-warm-b)"/>
      </linearGradient>
    </defs>
    <polygon points="0,0 756,0 756,220 0,402" fill="url(#storefront-tones)" role="img" aria-label="Photo of the Golden Harbour office storefront on a sunny street"/>
    <polygon points="0,402 756,218 756,246 0,430" fill="var(--orange)"/>
    <polygon points="40,430 300,376 300,1141 40,1141" fill="var(--navy)"/>
    <polygon points="0,1141 756,1141 756,1200 0,1200" fill="var(--orange)"/>
    <polygon points="334,516 692,516 676,592 322,592" fill="var(--navy)"/>
    <polygon points="540,1101 756,1101 756,1145 508,1145" fill="var(--navy)"/>
  </svg>

  <header class="brand">
    <div class="brand-mark"></div>
    <div class="brand-name">Golden Harbour</div>
    <div class="brand-regions">Marbella Estepona Sotogrande</div>
    <div class="brand-web">www.golden-harbour.example</div>
  </header>

  <div class="gallery-photo" style="top:453px; background:linear-gradient(180deg,var(--photo-sky) 0%,#e9eef2 45%,var(--photo-pool) 70%,#9ec2a8 100%);" role="img" aria-label="Sold apartment complex with swimming pool"></div>
  <div class="gallery-photo" style="top:628px; background:linear-gradient(180deg,#2f7fd0 0%,#f2f4f6 40%,var(--photo-green) 70%,var(--photo-pool) 100%);" role="img" aria-label="Sold seafront residential building with pool"></div>
  <div class="gallery-photo" style="top:805px; background:linear-gradient(180deg,#4a9ae0 0%,#eef0ee 40%,var(--photo-green) 65%,var(--photo-pool) 100%);" role="img" aria-label="Sold villa development with garden and pool"></div>
  <div class="gallery-photo" style="top:980px; background:linear-gradient(180deg,#f4efe6 0%,var(--photo-interior) 55%,#b27a46 100%);" role="img" aria-label="Interior of the Golden Harbour office"></div>

  <h1 class="headline">Sell with us !</h1>
  <p class="tagline">MAX PRICE &amp; FAST</p>

  <div class="extra-offer"><span>We also offer:</span><span>Maintenance &amp; Key holding</span></div>

  <h2 class="results-title">Curious how we get such good results?</h2>
  <ol class="results-list">
    <li class="results-group"><span>1. Complete, high quality presentation of your property</span>
      <div class="results-point"><svg width="10" height="8" viewBox="0 0 10 8"><path d="M1 4 L4 7 L9 1" stroke="var(--navy)" stroke-width="1.6" fill="none"/></svg>Stunning, professional photography</div>
      <div class="results-point"><svg width="10" height="8" viewBox="0 0 10 8"><path d="M1 4 L4 7 L9 1" stroke="var(--navy)" stroke-width="1.6" fill="none"/></svg>Home staging &amp; in-depth, multilingual descriptions 360° virtual tours, videos &amp; more</div>
    </li>
    <li class="results-group"><span>2. Promote your property in all imaginable ways</span>
      <div class="results-point"><svg width="10" height="8" viewBox="0 0 10 8"><path d="M1 4 L4 7 L9 1" stroke="var(--navy)" stroke-width="1.6" fill="none"/></svg>Property listed in the MLS network of realtors (2,000+ agencies)</div>
      <div class="results-point"><svg width="10" height="8" viewBox="0 0 10 8"><path d="M1 4 L4 7 L9 1" stroke="var(--navy)" stroke-width="1.6" fill="none"/></svg>Paid promotion in all major national &amp; international web portals</div>
      <div class="results-point"><svg width="10" height="8" viewBox="0 0 10 8"><path d="M1 4 L4 7 L9 1" stroke="var(--navy)" stroke-width="1.6" fill="none"/></svg>Creative &amp; social media marketing (Facelink, Chirper, Vidstream, etc.)</div>
    </li>
    <li class="results-group"><span>3. Let us handle everything - you can just relax</span>
      <div class="results-point"><svg width="10" height="8" viewBox="0 0 10 8"><path d="M1 4 L4 7 L9 1" stroke="var(--navy)" stroke-width="1.6" fill="none"/></svg>Leave the keys with us, and we will take care of everything</div>
      <div class="results-point"><svg width="10" height="8" viewBox="0 0 10 8"><path d="M1 4 L4 7 L9 1" stroke="var(--navy)" stroke-width="1.6" fill="none"/></svg>We will negotiate the best deal for you (look at our reviews)</div>
      <div class="results-point"><svg width="10" height="8" viewBox="0 0 10 8"><path d="M1 4 L4 7 L9 1" stroke="var(--navy)" stroke-width="1.6" fill="none"/></svg>Working 7 days a week (yes, even Sundays and evenings)</div>
    </li>
  </ol>

  <svg class="valuation-badge" viewBox="0 0 212 122" aria-hidden="true">
    <polygon points="190,32 212,34 206,98 184,98" fill="var(--orange)"/>
    <polygon points="10,0 196,32 188,100 0,122" fill="var(--navy)"/>
  </svg>
  <p class="valuation-text">Offer free<span>valuations</span></p>

  <div class="agent-photo" role="img" aria-label="Portrait of the listing agent Elena Marlow"></div>
  <p class="agent-name">Elena Marlow</p>

  <footer>
    <div class="footer-offices">
      <p>We have our offices located in San Luis de Sabinillas / Manilva, Costa del Sol, Spain.</p>
      <p>Languages we speak (Spanish, English, German, Russian, Ukrainian, Lithuanian, French, Italian, Danish, Polish)</p>
    </div>
    <div class="footer-contact">
      <p>(+34) 600 12 34 56</p>
      <p>elena@golden-harbour.example</p>
      <p>Calle Los Pinos 8, 29601 San Luis de Sabinillas</p>
    </div>
  </footer>
</main>
</body>
</html>
```